Company or website name
- www.brambletonhiregroup.example
- Links to the website
- Brambleton Hire Group
- Describe your company and organization and target audience
- We are a full service executive recruiting and staffing company. We work within all vertical markets within the US.
- The design should have the following
- Please ensure to include colors of the logo but feel free to include other colors as well to enhance the brochure. I'm looking for a single 8.5 x 11 inch brochure with front and back. The back will have more specific information while the front will be more a space for photos and general information on our company.
- Other Facts

```html
<!DOCTYPE html>
<html lang="en">
<head>
<meta charset="utf-8">
<title>Brambleton Hire Group – Brochure Front</title>
<link rel="stylesheet" href="https://fonts.googleapis.com/css2?family=Archivo+Black&family=Arimo:wght@700&family=Open+Sans:wght@400&display=swap">
<style>
  :root {
    --page: #ffffff;
    --brand-blue: #2c4f86;
    --band-dark: #3a3a3c;
    --panel-teal: #3e7f96;
    --accent-yellow: #f6f1a2;
    --text-light: #ffffff;
    --photo-light: #f1eff3;
    --photo-mid: #c9c4c6;
    --photo-dark: #4a4548;
  }
  * { margin: 0; padding: 0; box-sizing: border-box; }
  html, body { width: 875px; height: 1200px; overflow: hidden; background: var(--page); }
  .brochure { position: relative; width: 875px; height: 1200px; background: var(--page); }

  .brand {
    position: absolute; left: 129px; top: 66px; width: 383px; height: 103px;
    display: flex; align-items: center; gap: 14px; padding-left: 10px;
  }
  .brand-dot { width: 58px; height: 58px; border-radius: 50%; background: var(--brand-blue); flex: none; }
  .brand-name {
    font-family: "Arimo", Arial, sans-serif; font-weight: 700; font-size: 26px;
    color: var(--brand-blue); white-space: nowrap;
  }

  .hero-photo {
    position: absolute; left: 15px; top: 195px; width: 845px; height: 513px;
    background: linear-gradient(100deg, var(--photo-mid) 0%, var(--photo-light) 30%, #ddd8da 62%, var(--photo-dark) 100%);
  }
  .dark-band { position: absolute; left: 15px; top: 717px; width: 845px; height: 29px; background: var(--band-dark); }

  .info-panel { position: absolute; left: 15px; top: 746px; width: 845px; height: 437px; background: var(--panel-teal); }
  .tagline-lead {
    position: absolute; left: 265px; top: 26px;
    font-family: "Arimo", Arial, sans-serif; font-weight: 700; font-size: 35px;
    color: var(--text-light); letter-spacing: -0.3px; white-space: nowrap;
  }
  .tagline-main {
    position: absolute; left: 203px; top: 74px;
    font-family: "Archivo Black", "Arial Black", sans-serif; font-size: 92px;
    color: var(--accent-yellow); letter-spacing: -3px; line-height: 1; white-space: nowrap;
  }
  .mission {
    position: absolute; left: 14px; top: 218px; width: 790px;
    font-family: "Open Sans", Arial, sans-serif; font-size: 15px; line-height: 21px;
    color: var(--text-light);
  }
  .rule { position: absolute; left: 17px; top: 341px; width: 769px; height: 3px; background: var(--accent-yellow); }
  .site-link {
    position: absolute; right: 65px; top: 357px;
    font-family: "Arimo", Arial, sans-serif; font-weight: 700; font-size: 21px;
    color: var(--accent-yellow); text-decoration: none; white-space: nowrap;
  }
</style>
</head>
<body>
<main class="brochure">
  <div class="brand">
    <span class="brand-dot"></span>
    <span class="brand-name">Brambleton Hire Group</span>
  </div>

  <div class="hero-photo" role="img" aria-label="Photo of three smiling office professionals gathered around a laptop"></div>
  <div class="dark-band"></div>

  <section class="info-panel">
    <h2 class="tagline-lead">Whatever you're looking for</h2>
    <h1 class="tagline-main">we've got it</h1>
    <p class="mission">At Brambleton Hire Group, our mission is to match employers with employees to form successful work relationships. We succeed in our mission by providing excellent service to our clients and candidates, consistently meeting established expectations, and setting and maintaining the highest standards and ethics demonstrated in the employment services industry.</p>
    <div class="rule"></div>
    <a class="site-link" href="https://www.brambletonhiregroup.example">www.brambletonhiregroup.example</a>
  </section>
</main>
</body>
</html>
```